Larkspur Ridge Management - Business Cards

I need business cards. My current logo was designed by a designer at this site and I very much like and am happy with the results. I would like a business card that is trendy, unique, current yet professional. I deal with high net worth clients daily

Target Market(s)

Out of state investors looking to get into the rental market in Ohio

Industry/Entity Type

Property Management, Consulting

Contact Information for Business Card

Name, Title (Chief Financial Officer) office phone number (555) 817-3094 website address larkridgemgmt.example

Font styles to use
Sans Serif

Colors
0054AA
0677BA
7BADD7
CADEEF
E8F1F8
0094D4
00A9DD
6FCCEA
C7EBF8
E9F6FB
00AB8E
00BBA5
67D7C9
C6EFE9
E9F9F6

```html
<!DOCTYPE html>
<html lang="en">
<head>
<meta charset="utf-8">
<title>Larkspur Ridge Management – Business Cards</title>
<link rel="stylesheet" href="https://fonts.googleapis.com/css2?family=Figtree:wght@400;700&display=swap">
<style>
  :root {
    --navy: #223356;
    --red: #d42a35;
    --white: #ffffff;
    --backdrop: #ececec;
    --font: "Figtree", sans-serif;
  }
  html, body {
    margin: 0;
    padding: 0;
    width: 1200px;
    height: 1200px;
    overflow: hidden;
    background: var(--backdrop);
    font-family: var(--font);
  }
  .card {
    position: absolute;
    top: 169px;
    width: 494px;
    height: 862px;
    overflow: hidden;
  }
  .card--front { left: 90px; }
  .card--back { left: 616px; }
  .card__art {
    position: absolute;
    inset: 0;
    width: 100%;
    height: 100%;
  }
  .wordmark {
    position: absolute;
    left: 0;
    right: 0;
    margin: 0;
    text-align: center;
    color: var(--navy);
    font-weight: 700;
    font-size: 38px;
    line-height: 1.1;
    letter-spacing: 0.5px;
  }
  .card--front .wordmark { top: 130px; }
  .card--back .wordmark { top: 350px; }
  .contact {
    position: absolute;
    left: 0;
    right: 0;
    text-align: center;
    color: var(--white);
  }
  .contact__name {
    position: absolute;
    top: 590px;
    width: 100%;
    margin: 0;
    font-size: 38px;
    font-weight: 700;
  }
  .contact__title {
    position: absolute;
    top: 637px;
    width: 100%;
    margin: 0;
    font-size: 21px;
    font-weight: 400;
  }
  .contact__icons {
    position: absolute;
    top: 698px;
    left: 217px;
    width: 60px;
    height: 23px;
  }
  .contact__phone,
  .contact__web {
    position: absolute;
    width: 100%;
    margin: 0;
    font-size: 23px;
    font-weight: 400;
    letter-spacing: 0.5px;
  }
  .contact__phone { top: 733px; }
  .contact__web { top: 770px; }
</style>
</head>
<body>

<section class="card card--front" aria-label="Business card front">
  <svg class="card__art" viewBox="0 0 395 690" preserveAspectRatio="none" aria-hidden="true">
    <defs>
      <linearGradient id="front-glow" x1="0" y1="0" x2="1" y2="0">
        <stop offset="0" stop-color="#fff" stop-opacity="0"/>
        <stop offset="0.5" stop-color="#fff" stop-opacity="0.9"/>
        <stop offset="1" stop-color="#fff" stop-opacity="0"/>
      </linearGradient>
    </defs>
    <rect class="front-base" width="395" height="690" fill="var(--navy)"/>
    <polygon class="front-white-field" points="0,0 395,0 395,245 197,355 0,245" fill="var(--white)"/>
    <polygon class="front-red-chevron" points="0,245 197,355 395,245 395,278 197,388 0,278" fill="var(--red)"/>
    <polygon class="front-glow-chevron" points="48,322 197,405 347,322 347,342 197,428 48,342" fill="url(#front-glow)"/>
  </svg>

  <p class="wordmark">Larkspur Ridge<br>Management</p>

  <div class="contact">
    <p class="contact__name">Your Name</p>
    <p class="contact__title">Chief Financial Officer</p>
    <svg class="contact__icons" viewBox="0 0 60 23" aria-hidden="true">
      <rect x="1" y="1" width="58" height="21" rx="10.5" fill="none" stroke="var(--red)" stroke-width="1.6"/>
      <path class="icon-phone" d="M17 6.5c-.8 0-1.6.8-1.4 1.8.6 3.6 3.5 6.6 7.1 7.2 1 .2 1.8-.6 1.8-1.4l-.1-1.1-2.3-.8-1 1c-1.5-.7-2.7-1.9-3.4-3.4l1-1-.8-2.3z" fill="var(--red)"/>
      <g class="icon-globe" fill="none" stroke="var(--red)" stroke-width="1.2">
        <circle cx="40" cy="11.5" r="5.5"/>
        <ellipse cx="40" cy="11.5" rx="2.3" ry="5.5"/>
        <line x1="34.5" y1="11.5" x2="45.5" y2="11.5"/>
      </g>
    </svg>
    <p class="contact__phone">(555) 817-3094</p>
    <p class="contact__web">larkridgemgmt.example</p>
  </div>
</section>

<section class="card card--back" aria-label="Business card back">
  <svg class="card__art" viewBox="0 0 395 690" preserveAspectRatio="none" aria-hidden="true">
    <defs>
      <linearGradient id="back-glow" x1="0" y1="0" x2="1" y2="0">
        <stop offset="0" stop-color="#fff" stop-opacity="0"/>
        <stop offset="0.5" stop-color="#fff" stop-opacity="0.9"/>
        <stop offset="1" stop-color="#fff" stop-opacity="0"/>
      </linearGradient>
    </defs>
    <rect class="back-base" width="395" height="690" fill="var(--navy)"/>
    <polygon class="back-glow-top" points="48,185 197,62 347,185 347,165 197,80 48,165" fill="url(#back-glow)"/>
    <polygon class="back-red-diamond" points="0,275 197,102 395,275 395,432 197,538 0,432" fill="var(--red)"/>
    <polygon class="back-white-diamond" points="0,305 197,135 395,305 395,400 197,505 0,400" fill="var(--white)"/>
    <polygon class="back-glow-bottom" points="48,478 197,560 347,478 347,498 197,582 48,498" fill="url(#back-glow)"/>
  </svg>

  <p class="wordmark">Larkspur Ridge<br>Management</p>
</section>

</body>
</html>
```